Quiet Harbor
How Opening the Palate Renews Rest, Vigor, and Poise Without an Operation
Creative Brief
Description: I’m seeking a talented designer to create a professional, simple, and wellness-oriented cover for my upcoming book. The book explores the hidden connection between jaw expansion, airway health, and whole-body wellness. What I’m Looking For: Clean, minimalist style (similar to Tidal by Colin Marsby and The Lumen Method by Gregory Tallisant). A design that communicates both trustworthiness and transformation — this is a serious wellness/health book, not a textbook. Imagery that subtly conveys space, breathing, and expansion (abstract or symbolic — not literal medical images). Professional typography with good spacing and balance. A design that looks credible in both print and digital formats (Amazon, bookstore, audiobook). Deliverables: Front cover design (with title, subtitle, author name). Full jacket design (front, spine, back cover with provided text). Final files in print-ready PDF + high-res PNG/JPEG + source files (AI/PSD/INDD). About the Author: Dr. Darren Okafield, DMD, is a board-certified orthodontist and dentofacial orthopedist recognized internationally for his airway-focused approach. Featured in Plain Ease, Vantage Wellbeing, and BX Magazine, he helps patients achieve healthier smiles and better breathing without unnecessary surgery.
Health
Health minded people. Men and women but maybe lean a little more toward women
Design the front and back cover. Attached is a current design but I want to go with a new title subtitle of: Title: Open Passage Subtitle: The Quiet Link Among Inhaling, Rest, and Total Vitality ... I'm also open to other titles that might convey a similar message. Here is the back of the book description: What if the cause of your fatigue, poor sleep, anxiety, or lack of focus wasn’t in your mind—but in your mouth? Hidden jaw and airway problems affect millions of adults, yet most go undiagnosed. A narrow palate, mouth breathing, or underdeveloped jaws can quietly disrupt your health, appearance, and energy every single day. In this groundbreaking book, Dr. Darren Okafield—board-certified orthodontist, dentofacial orthopedist, airway-focused clinician, and author of The Kolvex Principle—reveals how your smile, facial balance, and airway are deeply connected to whole-body health. Through real patient stories, simple science, and clear explanations of modern treatment approaches, you’ll discover: The hidden epidemic of underdeveloped jaws and how it impacts breathing, sleep, wellness, and facial harmony Why mouth breathing is more than a bad habit—it’s a health disruptor The truth about palate expanders for adults and children (and what’s important to know about them) What to expect on your treatment journey, from first consultation to long-term results How better breathing can transform not only your health—but also your confidence and overall vitality This isn’t just about teeth. It’s about unlocking the power of proper breathing, creating balance in the face, and giving your body the space it needs to thrive. If you’ve ever felt like something was “off” with your health but couldn’t find the root cause, this book offers the missing link—and a guide to lasting transformation. About the Author Dr. Darren Okafield is a board-certified orthodontist and dentofacial orthopedist and founder of TrelbyBraceClinic.example. Recognized internationally for his airway-focused approach, he helps children, teens, and adults achieve healthier smiles and better breathing without unnecessary surgery. Featured in Plain Ease, Vantage Wellbeing, and with an upcoming expert feature in BX Magazine, he is passionate about educating both consumers and professionals on the life-changing connection between orthodontics, facial development, and whole-body health.

```html
<!DOCTYPE html>
<html lang="en">
<head>
<meta charset="utf-8">
<title>Open Passage — Book Jacket</title>
<link href="https://fonts.googleapis.com/css2?family=Montserrat:wght@500;700;800&family=Open+Sans:wght@400;600;700&display=swap" rel="stylesheet">
<style>
  :root {
    --paper: #ffffff;
    --spine: #eef3f4;
    --teal: #1f7f8f;
    --teal-band: #2c8c9b;
    --navy: #1c3550;
    --ink: #2f3a44;
    --muted: #6d7780;
    --rule: #d6dfe2;
  }
  html, body { margin: 0; padding: 0; overflow: hidden; }
  body { width: 1200px; height: 672px; background: var(--paper); }
  .jacket { position: relative; width: 1200px; height: 672px; background: var(--paper); font-family: "Open Sans", sans-serif; color: var(--ink); overflow: hidden; }

  /* Back cover */
  .back { position: absolute; left: 0; top: 0; width: 396px; height: 655px; padding: 14px 24px 0; box-sizing: border-box; }
  .back-heading { text-align: center; font-family: "Montserrat", sans-serif; font-weight: 700; color: var(--navy); margin: 0; }
  .back-heading .kicker { display: block; font-size: 11px; letter-spacing: 1px; text-transform: uppercase; }
  .back-heading .line { display: block; font-size: 13px; line-height: 17px; }
  .back-hook { margin: 12px 0 8px; font-family: "Montserrat", sans-serif; font-weight: 700; font-size: 9px; letter-spacing: .6px; color: var(--teal); text-transform: uppercase; }
  .back-copy p { margin: 0 0 7px; font-size: 7.6px; line-height: 11px; text-align: justify; }
  .author-box { position: absolute; left: 24px; top: 460px; display: flex; align-items: center; gap: 10px; }
  .author-photo { width: 46px; height: 46px; border-radius: 50%; background: linear-gradient(160deg, #c9d6da, #8fa6ad); }
  .author-box .name { font-size: 8.5px; font-weight: 700; color: var(--navy); line-height: 12px; }
  .author-box .role { font-size: 7px; color: var(--muted); line-height: 10px; }

  /* Spine */
  .spine { position: absolute; left: 396px; top: 0; width: 68px; height: 655px; background: var(--spine); border-left: 1px solid var(--rule); border-right: 1px solid var(--rule); }
  .spine-title, .spine-author { position: absolute; left: 50%; white-space: nowrap; font-family: "Montserrat", sans-serif; font-weight: 700; transform-origin: center; }
  .spine-title { top: 250px; font-size: 26px; letter-spacing: 2px; color: var(--teal); transform: translate(-50%, -50%) rotate(90deg); }
  .spine-author { top: 560px; font-size: 13px; letter-spacing: 1px; color: var(--navy); transform: translate(-50%, -50%) rotate(90deg); }

  /* Front cover */
  .front { position: absolute; left: 464px; top: 0; width: 736px; height: 655px; background: linear-gradient(180deg, #ffffff 60%, #eef5f6 100%); text-align: center; }
  .title { margin: 14px 0 0; font-family: "Montserrat", sans-serif; font-weight: 800; color: var(--teal); font-size: 70px; line-height: 66px; letter-spacing: 6px; }
  .title span { display: block; }
  .emblem-row { position: relative; height: 100px; margin-top: 14px; }
  .emblem { position: absolute; left: 50%; top: 0; width: 130px; height: 92px; margin-left: -65px; border-radius: 48% 48% 44% 44%; background: radial-gradient(circle at 50% 45%, #8fc6cf, #2c8c9b); }
  .side-note { position: absolute; top: 38px; width: 150px; font-family: "Montserrat", sans-serif; font-size: 9px; font-weight: 500; color: var(--muted); letter-spacing: .5px; text-transform: uppercase; line-height: 13px; }
  .side-note.left { left: 130px; }
  .side-note.right { right: 130px; }
  .subtitle { margin: 22px auto 0; width: 440px; font-weight: 700; color: var(--navy); font-size: 16px; line-height: 21px; }
  .tagline { margin: 18px auto 0; width: 420px; font-weight: 600; color: var(--ink); font-size: 13px; line-height: 18px; }
  .author { position: absolute; left: 0; right: 0; top: 548px; margin: 0; font-family: "Montserrat", sans-serif; font-weight: 700; font-size: 28px; letter-spacing: 1px; color: var(--navy); }
  .imprint { position: absolute; left: 0; right: 0; top: 590px; margin: 0; font-size: 9px; color: var(--muted); }

  .band { position: absolute; left: 0; bottom: 0; width: 1200px; height: 17px; background: var(--teal-band); }
</style>
</head>
<body>
<div class="jacket">

  <section class="back">
    <h2 class="back-heading">
      <span class="kicker">Discover the</span>
      <span class="line">quiet connection between</span>
      <span class="line">breathing and whole-body health</span>
    </h2>
    <p class="back-hook">Not just about teeth — it's about the space to breathe</p>
    <div class="back-copy">
      <p>What if the cause of your fatigue, poor sleep, anxiety, or lack of focus wasn't in your mind—but in your mouth? Hidden jaw and airway problems affect millions of adults, yet most go undiagnosed. A narrow palate, mouth breathing, or underdeveloped jaws can quietly disrupt your health, appearance, and energy every single day.</p>
      <p>In this groundbreaking book, Dr. Darren Okafield—board-certified orthodontist, dentofacial orthopedist, airway-focused clinician, and author of The Kolvex Principle—reveals how your smile, facial balance, and airway are deeply connected to whole-body health.</p>
      <p>Through real patient stories, simple science, and clear explanations of modern treatment approaches, you'll discover the hidden epidemic of underdeveloped jaws, why mouth breathing is more than a bad habit, the truth about palate expanders for adults and children, and what to expect on your treatment journey.</p>
      <p>This isn't just about teeth. It's about unlocking the power of proper breathing, creating balance in the face, and giving your body the space it needs to thrive.</p>
      <p>If you've ever felt like something was "off" with your health but couldn't find the root cause, this book offers the missing link—and a guide to lasting transformation.</p>
    </div>
    <div class="author-box">
      <div class="author-photo" role="img" aria-label="Author portrait"></div>
      <div>
        <div class="name">Dr. Darren Okafield</div>
        <div class="role">Orthodontist &amp; dentofacial orthopedist</div>
        <div class="role">TrelbyBraceClinic.example</div>
      </div>
    </div>
  </section>

  <aside class="spine">
    <div class="spine-title">OPEN PASSAGE</div>
    <div class="spine-author">OKAFIELD</div>
  </aside>

  <section class="front">
    <h1 class="title"><span>OPEN</span><span>PASSAGE</span></h1>
    <div class="emblem-row">
      <div class="side-note left">Less strain, more<br>connection</div>
      <div class="emblem" role="img" aria-label="Illustration of a brain with flowing airway lines"></div>
      <div class="side-note right">The path to free<br>breathing</div>
    </div>
    <p class="subtitle">The Quiet Link Among Inhaling, Rest, and Total Vitality</p>
    <p class="tagline">How opening the palate renews rest, vigor, and poise without an operation</p>
    <p class="author">DR. DARREN OKAFIELD</p>
    <p class="imprint">Orthodontist • Airway Clinician &amp; Author of The Kolvex Principle</p>
  </section>

  <div class="band"></div>
</div>
</body>
</html>
```